Carpet cleaning company focused on high quality needs business cards

We are a growing company that just merged with another company and need to design a new business card. We do both residential as well as commercial cleaning. We do carpet, tile & grout, upholstery, hard floors, and stain & pet odor removal. We treat our customers like family and strive to achieve outstanding results with every job.

```html
<!DOCTYPE html>
<html lang="en">
<head>
<meta charset="utf-8">
<title>Brightwell Floor Care — Business Cards</title>
<link rel="stylesheet" href="https://fonts.googleapis.com/css2?family=Open+Sans:wght@400;600;800&display=swap">
<style>
  :root {
    --backdrop: #8f8f8f;
    --brand-red: #f04842;
    --ink: #222222;
    --paper: #ffffff;
  }
  * { margin: 0; padding: 0; box-sizing: border-box; }
  html, body {
    width: 1200px; height: 1200px; overflow: hidden;
    background: var(--backdrop);
    font-family: "Open Sans", Arial, sans-serif;
  }
  .card {
    position: absolute;
    width: 797px; height: 464px;
    left: 200px;
  }
  .card--front { top: 90px; background: var(--brand-red); color: var(--paper); }
  .card--back { top: 624px; background: var(--paper); color: var(--ink); }

  .brand-art { position: absolute; }
  .card--front .brand-art { left: 95px; top: 82px; width: 254px; height: 302px; background: var(--paper); }
  .card--back .brand-art { left: 184px; top: 105px; width: 200px; height: 232px; background: var(--brand-red); }

  .wordmark {
    position: absolute;
    font-weight: 800;
    line-height: 1.1;
    white-space: nowrap;
  }
  .wordmark__line { display: block; }
  .card--front .wordmark { left: 406px; top: 82px; }
  .card--front .wordmark__line--main { font-size: 44px; }
  .card--front .wordmark__line--rest { font-size: 28px; }
  .card--back .wordmark { left: 401px; top: 222px; color: var(--ink); }
  .card--back .wordmark__line--main { font-size: 56px; }
  .card--back .wordmark__line--rest { font-size: 34px; }

  .person { position: absolute; left: 406px; top: 232px; }
  .person__name { font-size: 23px; font-weight: 800; letter-spacing: 0.2px; }
  .person__role { font-size: 16px; font-weight: 600; letter-spacing: 3.5px; margin-top: 2px; }

  .contact {
    position: absolute; left: 410px; top: 312px;
    list-style: none; font-size: 19px; line-height: 24px;
  }
  .contact__item { display: flex; align-items: center; gap: 8px; }
  .contact__icon { width: 14px; height: 14px; flex: none; }
</style>
</head>
<body>
  <section class="card card--front">
    <div class="brand-art" role="img" aria-label="Brand mascot area"></div>
    <div class="wordmark">
      <span class="wordmark__line wordmark__line--main">Brightwell</span>
      <span class="wordmark__line wordmark__line--rest">FLOOR CARE</span>
    </div>
    <div class="person">
      <p class="person__name">NAME SURNAME</p>
      <p class="person__role">POSITION</p>
    </div>
    <ul class="contact">
      <li class="contact__item">
        <svg class="contact__icon" viewBox="0 0 16 16" fill="#fff"><path d="M3.5 1l2.5 3-1.5 2c1 2 3 4 5 5l2-1.5 3 2.5-1.5 2.5C7 14 2 9 1 2.5z"/></svg>
        (555) 014-2290
      </li>
      <li class="contact__item">
        <svg class="contact__icon" viewBox="0 0 16 16" fill="none" stroke="#fff" stroke-width="1.5"><rect x="1.5" y="3.5" width="13" height="9"/><path d="M1.5 3.5l6.5 5 6.5-5"/></svg>
        info@brightwellfloor.com
      </li>
      <li class="contact__item">
        <svg class="contact__icon" viewBox="0 0 16 16" fill="none" stroke="#fff" stroke-width="1.3"><circle cx="8" cy="8" r="6.5"/><ellipse cx="8" cy="8" rx="3" ry="6.5"/><path d="M1.5 8h13"/></svg>
        brightwellfloor.com
      </li>
    </ul>
  </section>

  <section class="card card--back">
    <div class="brand-art" role="img" aria-label="Brand mascot area"></div>
    <div class="wordmark">
      <span class="wordmark__line wordmark__line--main">Brightwell</span>
      <span class="wordmark__line wordmark__line--rest">FLOOR CARE</span>
    </div>
  </section>
</body>
</html>
```